Lomi Vardell
Incorporated
Lomi Vardell -
Creative Brief
Use specific fonts
Please use font that would fulfill the requirements of the comment description below
Professional
Derek Holm
Operations Manager
City of Larkvale, CA
lomivardell@quillmesh.net
Our company extracts essential and fragrance oil from flowers. We blend our own brand-name perfume and fragrances. Please design cards to reflect a corporate appeal, with feminine luxury, higher end sophistication, yet gentle and soft. Attached is chosen logo. Feel free to take the abstract symbol and name out of the background if deemed necessary.

```html
<!DOCTYPE html>
<html lang="en">
<head>
<meta charset="utf-8">
<title>Lomi Vardell – Business Card</title>
<link href="https://fonts.googleapis.com/css2?family=Lato:wght@400;700;900&family=Cinzel:wght@400&display=swap" rel="stylesheet">
<style>
  :root {
    --backdrop: #e9e4dc;
    --card: #ffffff;
    --gold-mid: #d9c69c;
    --gold-deep: #a88a55;
    --ink: #111111;
    --brand-gold: #b08d57;
    --card-edge: #d8d2c6;
  }
  * { margin: 0; padding: 0; box-sizing: border-box; }
  html, body { width: 1200px; height: 529px; overflow: hidden; }
  body {
    background: var(--backdrop);
    font-family: "Lato", Arial, sans-serif;
    color: var(--ink);
    position: relative;
  }
  .card {
    position: absolute;
    top: 132px;
    width: 547px;
    height: 317px;
    background: var(--card);
    border: 1px solid var(--card-edge);
    overflow: hidden;
  }
  .card--front { left: 29px; }
  .card--back { left: 612px; }
  .card__swoop { position: absolute; inset: 0; width: 100%; height: 100%; }
  .holder { position: absolute; right: 28px; top: 28px; text-align: left; }
  .holder__name { font-size: 25px; font-weight: 900; line-height: 1.1; }
  .holder__title { font-size: 10px; font-weight: 400; margin-top: 3px; }
  .contact {
    position: absolute; left: 17px; top: 106px;
    font-size: 16px; font-weight: 700; line-height: 1.3;
  }
  .brand {
    position: absolute;
    display: flex; align-items: center;
    flex-direction: column;
    color: var(--brand-gold);
  }
  .brand--front { top: 224px; left: 230px; right: 20px; }
  .brand__dot {
    width: 44px; height: 44px; border-radius: 50%;
    background: radial-gradient(circle at 35% 35%, var(--gold-mid), var(--gold-deep));
  }
  .brand__name {
    font-family: "Cinzel", Georgia, serif;
    font-size: 15px; letter-spacing: 3px; margin-top: 10px;
  }
  .brand--back { top: 58px; left: 0; right: 0; }
  .brand--back .brand__dot { width: 100px; height: 100px; }
  .brand--back .brand__name { font-size: 16px; letter-spacing: 4px; margin-top: 10px; }
  .back-email {
    position: absolute; left: 0; right: 0; top: 228px;
    text-align: center; font-size: 24px; font-weight: 700;
  }
</style>
</head>
<body>
  <section class="card card--front">
    <svg class="card__swoop" viewBox="0 0 547 317" preserveAspectRatio="none" aria-hidden="true">
      <defs>
        <radialGradient id="goldField" cx="0.45" cy="0.35" r="0.7">
          <stop offset="0" stop-color="#ffffff"/>
          <stop offset="0.35" stop-color="#ece0c2"/>
          <stop offset="1" stop-color="#a88a55"/>
        </radialGradient>
      </defs>
      <path d="M0,0 H547 C430,30 390,150 270,190 C160,225 60,235 0,300 Z" fill="#8d8d8d"/>
      <path d="M0,0 H547 C430,22 385,138 265,176 C155,212 55,222 0,286 Z" fill="url(#goldField)"/>
    </svg>
    <div class="holder">
      <p class="holder__name">Derek Holm</p>
      <p class="holder__title">Operations Manager</p>
    </div>
    <div class="contact">
      <p>City of Larkvale, CA</p>
      <p>Pone: (949)555-0142</p>
      <p>Email: lomivardell@quillmesh.net</p>
    </div>
    <div class="brand brand--front">
      <span class="brand__dot"></span>
      <span class="brand__name">LOMIVARDELL</span>
    </div>
  </section>

  <section class="card card--back">
    <div class="brand brand--back">
      <span class="brand__dot"></span>
      <span class="brand__name">LOMIVARDELL</span>
    </div>
    <p class="back-email">Email: lomivardell@quillmesh.net</p>
  </section>
</body>
</html>
```